Bold Modern Creative Wine Label Needed for a Chardonnay

We need a modern, eye catching label, one that will appeal to millennials, but also attract the older more conservative crowd. We like the boldness of black on white but are open to your suggestions. Since the bottle type is a light green 'burgundy style' bottle, you should take that into account. The name of the brand is Vo`. The attached label is example of what we like very much. It is eye catching and bold and modern. Keep in mind that the bottle will be light green in color so black and white might not work so well. Use your creativity please! The label can be any size but needs to fit on this shape bottle. See attached photos. thanks!!

(Please no grapes or wine glasses or wine bottles featured on the label!)
Updates

Hi Designers, I just wanted to let you know that we received many great designs and we are sorting through them this week. The website is making it a bit difficult to create a 'poll' so this is taking longer than we expected. Thanks for all the great submissions!

```html
<!DOCTYPE html>
<html lang="en">
<head>
<meta charset="utf-8">
<title>Vo` Chardonnay Label</title>
<link rel="stylesheet" href="https://fonts.googleapis.com/css2?family=Questrial&family=Arimo:wght@700&display=swap">
<style>
  :root {
    --frame: #5b5c5e;
    --paper: #f4f4f4;
    --paper-edge: #e6e6e6;
    --ink: #333333;
    --ink-soft: #3a3a3a;
    --accent-light: #d4e24a;
    --accent-deep: #9bb83a;
    --accent-dark: #1d1d1d;
  }
  html, body {
    margin: 0;
    padding: 0;
    width: 1200px;
    height: 1178px;
    overflow: hidden;
    background: var(--frame);
  }
  .label {
    position: relative;
    width: 1200px;
    height: 1178px;
    background: var(--frame);
  }
  .label-panel {
    position: absolute;
    left: 54px;
    top: 66px;
    width: 1092px;
    height: 1072px;
    background: radial-gradient(ellipse at center, var(--paper) 0%, var(--paper-edge) 100%);
  }
  .hero-illustration {
    position: absolute;
    left: 462px;
    top: 180px;
    width: 168px;
    height: 426px;
    border-radius: 84px 84px 12px 12px;
    background: linear-gradient(180deg, var(--accent-light) 0%, var(--accent-deep) 38%, #8c8f6a 55%, var(--accent-dark) 100%);
  }
  .brand-name {
    position: absolute;
    left: 414px;
    top: 585px;
    margin: 0;
    font-family: "Questrial", sans-serif;
    font-weight: 400;
    font-size: 260px;
    line-height: 1;
    color: var(--ink);
    letter-spacing: -4px;
  }
  .winery-line {
    position: absolute;
    left: 658px;
    top: 879px;
    margin: 0;
    font-family: "Questrial", sans-serif;
    font-size: 45px;
    line-height: 1;
    color: var(--ink-soft);
  }
  .since-line {
    position: absolute;
    left: 660px;
    top: 973px;
    margin: 0;
    font-family: "Arimo", sans-serif;
    font-weight: 700;
    font-size: 33px;
    line-height: 1;
    color: var(--ink);
    letter-spacing: 0.5px;
  }
  .volume-line {
    position: absolute;
    left: 418px;
    top: 1054px;
    margin: 0;
    font-family: "Arimo", sans-serif;
    font-weight: 700;
    font-size: 39px;
    line-height: 1;
    color: var(--ink);
  }
</style>
</head>
<body>
  <main class="label">
    <div class="label-panel" role="img" aria-label="Soft light grey decorative background texture"></div>
    <div class="hero-illustration" role="img" aria-label="Central illustration area in fresh green tones fading to black"></div>
    <h1 class="brand-name">Vo`</h1>
    <p class="winery-line">By Vo` Winery</p>
    <p class="since-line">SINCE 2009</p>
    <p class="volume-line">12% ALC VOL 750ml</p>
  </main>
</body>
</html>
```